Morden, Creative, Unique, Independent Wine Shop

1. We are a brand new wine shop located in Melbourne Australia, we have our logo already, simply use the logo to design a business card.
2. I have uploaded our logo in two versions, with or without shadow, any of them is acceptable.
3. Make it as creative and unique as possible, no limitation of shape, color combination, geometry pattern, fonts, composing etc.
3. Info on the card:
- Brambleford Wine Cellar (Not very necessary if logo is obviously shown)
- 42 Ferncastle Steet, Hampton, Victoria, Australia 3188
- +61 3 9018 4637
- www.bramblefordwinecellar.com.au
- bramblefordwinecellar@mailvista.com
- Additional icons: Google, Instagram, Facebook, Twitter
4. Once again, forget it is a commercial card, make it special.

```html
<!DOCTYPE html>
<html lang="en">
<head>
<meta charset="utf-8">
<title>Brambleford Wine Cellar – Business Card</title>
<link rel="stylesheet" href="https://fonts.googleapis.com/css2?family=Source+Sans+3:wght@400;600&display=swap">
<style>
  :root {
    --page-bg: #f2f2f2;
    --card-dark: #231f20;
    --wine: #b31b43;
    --wine-deep: #8c1232;
    --grey-mid: #8a8a8a;
    --white: #ffffff;
    --pill: #231f20;
    --contact-text: #f1c9d4;
  }
  * { margin: 0; padding: 0; box-sizing: border-box; }
  html, body { width: 1200px; height: 1200px; overflow: hidden; }
  body {
    background: var(--page-bg);
    position: relative;
    font-family: "Source Sans 3", "Myriad Pro", Arial, sans-serif;
  }
  .card {
    position: absolute;
    width: 474px;
    height: 268px;
    overflow: hidden;
  }
  .card--front { left: 355px; top: 154px; background: var(--card-dark); }
  .card--back  { left: 356px; top: 748px; background: var(--wine); }

  .brand-dot {
    position: absolute;
    left: 50%;
    transform: translateX(-50%);
    border-radius: 50%;
  }
  .card--front .brand-dot { top: 58px; width: 64px; height: 64px; background: var(--grey-mid); }
  .card--back .brand-dot { top: 46px; width: 44px; height: 44px; background: var(--white); }

  .brand-rule {
    position: absolute;
    left: 133px;
    top: 176px;
    width: 208px;
    height: 1px;
    background: var(--grey-mid);
  }
  .brand-name {
    position: absolute;
    left: 0;
    width: 100%;
    text-align: center;
    font-weight: 400;
    letter-spacing: 1px;
    line-height: 1.05;
    text-transform: uppercase;
  }
  .card--front .brand-name { top: 184px; font-size: 31px; color: var(--wine); }
  .card--back .brand-name { top: 108px; font-size: 31px; color: var(--white); }

  .social-row {
    position: absolute;
    left: 13px;
    top: 12px;
    display: flex;
    gap: 5px;
  }
  .social-row span {
    width: 12px;
    height: 12px;
    background: var(--white);
    border-radius: 2px;
  }

  .address-line {
    position: absolute;
    left: 0;
    top: 216px;
    width: 100%;
    height: 1px;
    background: var(--card-dark);
  }
  .address-pill {
    position: absolute;
    left: 59px;
    top: 206px;
    width: 354px;
    height: 21px;
    border-radius: 11px;
    background: var(--pill);
    color: var(--white);
    font-size: 13px;
    line-height: 21px;
    text-align: center;
  }
  .contact-row {
    position: absolute;
    left: 0;
    top: 238px;
    width: 100%;
    display: flex;
    justify-content: center;
    gap: 12px;
    font-size: 10.5px;
    color: var(--contact-text);
  }
  .contact-item { display: flex; align-items: center; gap: 4px; white-space: nowrap; }
  .contact-item svg { width: 11px; height: 11px; fill: none; stroke: var(--white); stroke-width: 1.6; }
</style>
</head>
<body>

  <section class="card card--front" aria-label="Card front">
    <div class="brand-dot"></div>
    <div class="brand-rule"></div>
    <div class="brand-name">Brambleford<br>Wine Cellar</div>
  </section>

  <section class="card card--back" aria-label="Card back">
    <div class="social-row" aria-label="Social links">
      <span></span><span></span><span></span><span></span>
    </div>
    <div class="brand-dot"></div>
    <div class="brand-name">Brambleford<br>Wine Cellar</div>

    <div class="address-line"></div>
    <div class="address-pill">42 Ferncastle Steet, Hampton, Victoria, Australia 3188</div>

    <div class="contact-row">
      <span class="contact-item">
        <svg viewBox="0 0 12 12"><path d="M3 1.5 L4.8 4 L3.8 5.2 Q5 7.4 6.8 8.2 L8 7.2 L10.5 9 L9.5 10.5 Q4.5 10 1.5 3 Z" fill="#fff" stroke="none"/></svg>
        +61 3 9018 4637
      </span>
      <span class="contact-item">
        <svg viewBox="0 0 12 12"><circle cx="6" cy="6" r="4.8"/><ellipse cx="6" cy="6" rx="2" ry="4.8"/><line x1="1.2" y1="6" x2="10.8" y2="6"/></svg>
        www.bramblefordwinecellar.com.au
      </span>
      <span class="contact-item">
        <svg viewBox="0 0 12 12"><rect x="1" y="2.5" width="10" height="7" fill="#fff" stroke="none"/><path d="M1 2.5 L6 6.5 L11 2.5" stroke="#b31b43" stroke-width="1"/></svg>
        bramblefordwinecellar@mailvista.com
      </span>
    </div>
  </section>

</body>
</html>
```